Pawlume Tonic - Functtional water for dogs. Brand new product

I have a design alreday. It needs an upgrade. I need it in two steps. One that sums everything in 5 pges and one as the one as sent as the longer brief. So one that is a full version and one summary. I want it to be rea professional for a presentation to investors, stores etc. Important to make the same thur out the presentation so it feels like it belongs together. High end business but still modern for a brand new unique product. The first product on the market is Morning Brinefix (the other 3 mighgt come later on). Its in Sweden we start like a city like stockholm. Important that its realistic. Not to dark. Again think towards high end investors.

Target Market(s)

The presentation is for investors och businesses. The product is for dogowners who keep their animals as family members, active people, city people, people who travel etc

Industry/Entity Type

Dogs och dog food and vitamins

Requirements
Must have
• High end but still modern and breathe a brand new product thats unique. For investors that will invest money in this project.

```html
<!DOCTYPE html>
<html lang="en">
<head>
<meta charset="utf-8">
<title>Pawlume Tonic – Go-to-Market Strategy</title>
<link href="https://fonts.googleapis.com/css2?family=Poppins:wght@400;500;600;700;800&display=swap" rel="stylesheet">
<style>
  :root {
    --navy: #0b2f7e;
    --navy-deep: #062a78;
    --sky: #9dbfe0;
    --slide: #f3f4f5;
    --card: #e6e6e7;
    --muted: #5a6270;
    --white: #ffffff;
  }
  * { box-sizing: border-box; margin: 0; padding: 0; }
  html, body {
    width: 1200px; height: 1001px; overflow: hidden;
    background: var(--slide);
    font-family: "Poppins", sans-serif;
    color: var(--navy);
  }
  .slide { position: relative; width: 1200px; height: 1001px; }

  .brand {
    position: absolute; left: 66px; top: 250px;
    display: flex; align-items: center; gap: 12px;
  }
  .brand-dot { width: 34px; height: 34px; border-radius: 50%; background: var(--navy); }
  .brand-name {
    font-weight: 700; font-size: 31px; line-height: 30px; color: var(--navy);
  }

  .title {
    position: absolute; left: 0; width: 1200px; top: 318px;
    text-align: center; font-weight: 700; font-size: 46px; letter-spacing: 0.5px;
    color: var(--navy); line-height: 1.1;
  }
  .title-rule {
    position: absolute; left: 283px; width: 634px; top: 381px; height: 5px;
    background: var(--sky);
  }
  .intro {
    position: absolute; left: 0; width: 1200px; top: 410px;
    text-align: center; font-weight: 500; font-size: 15.5px; color: var(--muted);
  }

  .phases { position: absolute; left: 155px; top: 471px; display: flex; gap: 32px; }
  .phase {
    width: 275px; height: 201px; border-radius: 12px; background: var(--card);
    overflow: hidden;
  }
  .phase-head {
    height: 54px; background: var(--navy-deep); color: var(--white);
    display: flex; align-items: center; justify-content: center;
    font-weight: 700; font-size: 15px;
  }
  .phase-list { list-style: none; padding: 17px 0 0 18px; }
  .phase-list li {
    display: flex; align-items: center; gap: 9px; height: 36px;
    font-size: 17px; font-weight: 400; color: var(--navy); white-space: nowrap;
  }
  .bullet-icon { width: 19px; height: 19px; flex: none; }

  .closing {
    position: absolute; left: 226px; width: 748px; top: 702px; height: 54px;
    border-radius: 7px; background: var(--navy-deep); color: var(--white);
    display: flex; align-items: center; justify-content: center;
    font-weight: 700; font-size: 16px;
  }
</style>
</head>
<body>
<main class="slide">
  <div class="brand">
    <span class="brand-dot"></span>
    <span class="brand-name">pawlume<br>tonic</span>
  </div>

  <h1 class="title">GO-TO-MARKET STRATEGY</h1>
  <div class="title-rule"></div>
  <p class="intro">Pawlume Tonic follows a phased expansion strategy designed to build credibility before scaling distribution.</p>

  <section class="phases">
    <article class="phase">
      <h2 class="phase-head">PHASE 1 - CREDIBILITY</h2>
      <ul class="phase-list">
        <li><svg class="bullet-icon" viewBox="0 0 20 20"><circle cx="10" cy="10" r="10" fill="#0b2f7e"/><path d="M5.5 10 10 6l4.5 4v4.5h-9z" fill="none" stroke="#fff" stroke-width="1.2"/><path d="M10 9.5v3M8.5 11h3" stroke="#fff" stroke-width="1.1"/></svg>Veterinary Clinics</li>
        <li><svg class="bullet-icon" viewBox="0 0 20 20"><circle cx="10" cy="10" r="10" fill="#0b2f7e"/><path d="M5.5 8.5h9l-1-2.5h-7zM6.5 8.5v5.5h7V8.5" fill="none" stroke="#fff" stroke-width="1.2"/></svg>Pet Specialty Stores</li>
        <li><svg class="bullet-icon" viewBox="0 0 20 20"><circle cx="10" cy="10" r="10" fill="#0b2f7e"/><rect x="6.3" y="6" width="7.4" height="5.5" fill="none" stroke="#fff" stroke-width="1.2"/><path d="M5 13.5h10" stroke="#fff" stroke-width="1.3"/></svg>E-Commerce</li>
      </ul>
    </article>
    <article class="phase">
      <h2 class="phase-head">PHASE 2 - LIFESTYLE</h2>
      <ul class="phase-list">
        <li><svg class="bullet-icon" viewBox="0 0 20 20"><circle cx="10" cy="10" r="10" fill="#0b2f7e"/><path d="M5.5 14V8h3v6M8.5 14V6h4v8M12.5 14v-4h2v4M5 14h10" fill="none" stroke="#fff" stroke-width="1.1"/></svg>Premium Hotels</li>
        <li><svg class="bullet-icon" viewBox="0 0 20 20"><circle cx="10" cy="10" r="10" fill="#0b2f7e"/><path d="M8 5.5v9M6.8 5.5v3.2h2.4V5.5M12 14.5V5.5c1.3.8 1.3 3.4 0 4.2" fill="none" stroke="#fff" stroke-width="1.1"/></svg>Dog-friendly Restaurants</li>
        <li><svg class="bullet-icon" viewBox="0 0 20 20"><circle cx="10" cy="10" r="10" fill="#0b2f7e"/><path d="M5.5 12.5 14.5 6M9 9.5l-3-1.5M11 11l.5 3M7 13.5l-1.5 1" fill="none" stroke="#fff" stroke-width="1.2" stroke-linecap="round"/></svg>Travel &amp; Airport Retail</li>
      </ul>
    </article>
    <article class="phase">
      <h2 class="phase-head">PHASE 3 - SCALE</h2>
      <ul class="phase-list">
        <li><svg class="bullet-icon" viewBox="0 0 20 20"><circle cx="10" cy="10" r="10" fill="#0b2f7e"/><path d="M5 6h1.6l1.2 5.5h5.4l1-4H7.2" fill="none" stroke="#fff" stroke-width="1.1"/><circle cx="8.3" cy="13.6" r=".9" fill="#fff"/><circle cx="12.6" cy="13.6" r=".9" fill="#fff"/></svg>National Grocery Chains</li>
        <li><svg class="bullet-icon" viewBox="0 0 20 20"><circle cx="10" cy="10" r="10" fill="#0b2f7e"/><circle cx="10" cy="10" r="4.6" fill="none" stroke="#fff" stroke-width="1.1"/><ellipse cx="10" cy="10" rx="2" ry="4.6" fill="none" stroke="#fff" stroke-width="1"/><path d="M5.4 10h9.2" stroke="#fff" stroke-width="1"/></svg>European Expansion</li>
        <li><svg class="bullet-icon" viewBox="0 0 20 20"><circle cx="10" cy="10" r="10" fill="#0b2f7e"/><rect x="8.5" y="5" width="3" height="2.6" fill="none" stroke="#fff" stroke-width="1"/><rect x="4.8" y="12" width="3" height="2.6" fill="none" stroke="#fff" stroke-width="1"/><rect x="12.2" y="12" width="3" height="2.6" fill="none" stroke="#fff" stroke-width="1"/><path d="M10 7.6v2.4M6.3 12v-2h7.4v2" fill="none" stroke="#fff" stroke-width="1"/></svg>Broad Distributor Network</li>
      </ul>
    </article>
  </section>

  <p class="closing">This approach minimizes risk while creating sustainable long-term growth.</p>
</main>
</body>
</html>
```